Business Card Design

we are a brand new cable TV network devoted to self improvement and leading a better life called FLOURIVO TV.I have a logo. We have 3 executives that need cards.I want it to be a heavy stock card: professional but showing our creative nature

Industry/Entity Type

Business

Contact Information for Business Card

CLAUDIA SAENZ AMLIECEO350 San Juan DrPonte Vedra Beach FL 32082904-473-5953

```html
<!DOCTYPE html>
<html lang="en">
<head>
<meta charset="utf-8">
<title>FLOURIVO TV – Business Card</title>
<link rel="stylesheet" href="https://fonts.googleapis.com/css2?family=Roboto:wght@300;400;700;900&display=swap">
<style>
  :root {
    --backdrop: #1d1d1f;
    --card-white: #f3f3f3;
    --brand-red: #cf3a48;
    --brand-red-light: #d9505c;
    --ink-dark: #2b2b2d;
    --panel-text: #ffffff;
    --panel-text-soft: rgba(255,255,255,0.85);
  }
  * { box-sizing: border-box; margin: 0; padding: 0; }
  html, body {
    width: 1200px;
    height: 900px;
    overflow: hidden;
    background: var(--backdrop);
    font-family: "Roboto", Arial, sans-serif;
  }
  .stage {
    width: 1200px;
    height: 900px;
    display: flex;
    align-items: center;
    justify-content: center;
  }
  .business-card {
    position: relative;
    width: 1000px;
    height: 580px;
    background: var(--card-white);
    overflow: hidden;
  }
  .contact-panel {
    position: absolute;
    left: 0;
    top: 190px;
    width: 500px;
    height: 330px;
    background: linear-gradient(135deg, var(--brand-red) 0%, var(--brand-red-light) 100%);
    border-radius: 0 34px 34px 0;
    padding: 62px 0 0 64px;
    color: var(--panel-text);
  }
  .contact-name {
    font-weight: 900;
    font-size: 30px;
    letter-spacing: 0.5px;
    line-height: 1.1;
  }
  .contact-role {
    font-weight: 300;
    font-size: 17px;
    letter-spacing: 1px;
    margin-top: 6px;
    color: var(--panel-text-soft);
  }
  .contact-details {
    list-style: none;
    margin-top: 22px;
    font-weight: 400;
    font-size: 18px;
    letter-spacing: 1.5px;
    line-height: 1.55;
    color: var(--panel-text-soft);
  }
  .contact-phone {
    display: flex;
    align-items: center;
    gap: 10px;
  }
  .phone-icon { width: 14px; height: 14px; fill: var(--panel-text-soft); }
  .brand-name {
    position: absolute;
    left: 560px;
    top: 300px;
    display: flex;
    align-items: center;
    gap: 18px;
  }
  .brand-dot {
    width: 34px;
    height: 34px;
    border-radius: 50%;
    background: var(--brand-red);
  }
  .brand-wordmark {
    font-weight: 700;
    font-size: 54px;
    letter-spacing: -0.5px;
    color: var(--ink-dark);
  }
</style>
</head>
<body>
  <main class="stage">
    <article class="business-card">
      <section class="contact-panel">
        <h1 class="contact-name">MIRELLA OKAFOR DUNST</h1>
        <p class="contact-role">CEO</p>
        <ul class="contact-details">
          <li>718 Harlow Creek Dr</li>
          <li>Calder Sands Bay NC 28471</li>
          <li class="contact-phone">
            <svg class="phone-icon" viewBox="0 0 24 24" aria-hidden="true">
              <path d="M6.6 10.8a15.1 15.1 0 0 0 6.6 6.6l2.2-2.2c.3-.3.7-.4 1-.2 1.1.4 2.3.6 3.6.6.6 0 1 .4 1 1V20c0 .6-.4 1-1 1A17 17 0 0 1 3 4c0-.6.4-1 1-1h3.5c.6 0 1 .4 1 1 0 1.3.2 2.5.6 3.6.1.3 0 .7-.2 1z"/>
            </svg>
            742-618-2047
          </li>
        </ul>
      </section>
      <div class="brand-name">
        <span class="brand-dot" aria-hidden="true"></span>
        <span class="brand-wordmark">FLOURIVO TV</span>
      </div>
    </article>
  </main>
</body>
</html>
```